Tovrani IT business needs logo and business card designed

I need designed business card. it needs to have some wow effect, but simple, corporate and business focused. We provide corporate grade IT services to medium size businesses. These services are IT support over phone, email, in person, VOIP services, IT security , networking - everything that helps business be productivy.

Out tag line will be something along these lines" promoting business growth through use of technology:.

I need a logo designed as well. I am happy to use any colors/theme, perhaps neutral colours, earthy?

Priority: NICE looking, wow design, nice fonts, colors etc... nice logo, business focused but HAS to be modern, wow effect. I will accept anything that looks really cool.

Target Market(s)

Target market are businesses with 20-100 employees. Audience are business decision makers, like general managers, CEO, directors, those are the one seeing this business card;

Industry/Entity Type

Business

Contact Information for Business Card

I am totally flexible, suprise me me something creative:

Dorian Velmek logo on this side(you will design)
managing director ------------------------------- this is line
slogan: technology.delivered.simple

Level 3, 48 Pemberwick Street, Sydney, NSW 2000
dorian@tovrani.com.au
www.tovrani.com.au

back page: logo and slogan: promoting business growth through use of technolog

Requirements
Must have
• Must look modern, cool., wow effect, yet simple and professional.

```html
<!DOCTYPE html>
<html lang="en">
<head>
<meta charset="utf-8">
<title>Tovrani IT — Business Card</title>
<link rel="stylesheet" href="https://fonts.googleapis.com/css2?family=Open+Sans:wght@600;700&family=Questrial&display=swap">
<style>
  :root {
    --page: #ffffff;
    --teal: #4aa5a1;
    --ink-dark: #1e1e1e;
    --tile-dark: #262626;
    --tile-light: #303030;
    --white: #ffffff;
    --mark: #2b2b2b;
  }
  html, body {
    margin: 0;
    padding: 0;
    width: 1200px;
    height: 1200px;
    overflow: hidden;
    background: var(--page);
  }
  .canvas {
    position: relative;
    width: 1200px;
    height: 1200px;
  }
  .card {
    position: absolute;
    width: 498px;
    height: 807px;
    overflow: hidden;
  }
  .card--back { left: 85px; top: 89px; }
  .card--front { left: 616px; top: 303px; }

  .texture {
    position: absolute;
    inset: 0;
    background: radial-gradient(ellipse at 50% 40%, var(--tile-light) 0%, var(--tile-dark) 55%, var(--ink-dark) 100%);
  }
  .band {
    position: absolute;
    left: 0;
    width: 100%;
    background: var(--teal);
  }
  .brand-name {
    font-family: "Open Sans", sans-serif;
    font-weight: 700;
    color: var(--white);
    letter-spacing: -0.5px;
    margin: 0;
    white-space: nowrap;
  }
  .brand-dot {
    display: block;
    border-radius: 50%;
    background: var(--mark);
  }
  .tagline {
    font-family: "Open Sans", sans-serif;
    font-weight: 700;
    font-size: 25px;
    color: var(--white);
    text-align: center;
    margin: 0;
    line-height: 71px;
    white-space: nowrap;
  }

  /* Back side */
  .card--back .band--logo {
    top: 207px;
    height: 144px;
    display: flex;
    align-items: center;
    justify-content: center;
    gap: 18px;
  }
  .card--back .brand-dot { width: 40px; height: 40px; }
  .card--back .brand-name { font-size: 56px; }
  .band--tagline { bottom: 0; height: 71px; }

  /* Front side */
  .card--front .band--logo {
    top: 0;
    height: 241px;
  }
  .card--front .brand-dot {
    position: absolute;
    left: 50%;
    top: 44px;
    width: 58px;
    height: 58px;
    margin-left: -29px;
  }
  .card--front .brand-name {
    position: absolute;
    left: 0;
    right: 0;
    top: 128px;
    text-align: center;
    font-size: 54px;
    padding-left: 36px;
  }
  .contact {
    position: absolute;
    left: 44px;
    top: 400px;
    font-family: "Questrial", sans-serif;
    color: var(--white);
  }
  .person-name {
    font-size: 57px;
    font-weight: 400;
    margin: 0;
    line-height: 1;
    letter-spacing: 0.5px;
  }
  .person-role {
    font-size: 28px;
    color: var(--teal);
    margin: 10px 0 0 3px;
    letter-spacing: 0.5px;
  }
  .contact-list {
    margin: 22px 0 0 0;
    display: grid;
    grid-template-columns: 70px auto;
    row-gap: 6px;
    align-items: baseline;
  }
  .contact-list dt {
    font-size: 26px;
    color: var(--teal);
  }
  .contact-list dd {
    margin: 0;
    font-size: 19px;
  }
  .address {
    font-style: normal;
    margin: 20px 0 0 0;
    font-size: 19px;
    line-height: 25px;
  }
  .address .city {
    display: block;
    color: var(--teal);
    padding-left: 24px;
    font-size: 21px;
  }
</style>
</head>
<body>
<main class="canvas">

  <section class="card card--back" aria-label="Card back">
    <div class="texture" role="img" aria-label="Dark mosaic tile texture background"></div>
    <div class="band band--logo">
      <span class="brand-dot" aria-hidden="true"></span>
      <p class="brand-name">Tovrani IT</p>
    </div>
    <div class="band band--tagline">
      <p class="tagline">Technology.Made.Dependable</p>
    </div>
  </section>

  <section class="card card--front" aria-label="Card front">
    <div class="texture" role="img" aria-label="Dark mosaic tile texture background"></div>
    <div class="band band--logo">
      <span class="brand-dot" aria-hidden="true"></span>
      <p class="brand-name">Tovrani IT</p>
    </div>

    <div class="contact">
      <h1 class="person-name">Dorian Velmek</h1>
      <p class="person-role">Managing Director</p>
      <dl class="contact-list">
        <dt>Web</dt><dd>www.tovrani.com.au</dd>
        <dt>Mail</dt><dd>dorian@tovrani.com.au</dd>
      </dl>
      <address class="address">
        Level 7, 48 Pemberwick Street,
        <span class="city">Marlow Bay, NSW 2417</span>
      </address>
    </div>

    <div class="band band--tagline">
      <p class="tagline">Technology.Made.Dependable</p>
    </div>
  </section>

</main>
</body>
</html>
```